Business Card Design

Certified Canine Therapeutic Massage Practitioner
Specializing in Senior Canine Massage Therapy and Giant Breeds
Certified in Canine Emergency CPR, First Aid 7 Care

Target Market(s)

Dog lovers with disposable income.

Industry/Entity Type

Business

Contact Information for Business Card

Paws Unwound Studio
614.382.5097
Cedar Hollow, TN
Rulo@Pawsunwoundstudio.com

```html
<!DOCTYPE html>
<html lang="en">
<head>
<meta charset="utf-8">
<title>Paws Unwound Studio – Business Card</title>
<link rel="stylesheet" href="https://fonts.googleapis.com/css2?family=Delius&display=swap">
<style>
  :root {
    --backdrop: #2b2b2d;
    --peach: #eac2a3;
    --peach-ring: #e3b48f;
    --sky: #c4e1f4;
    --sky-pill: #b9dcf2;
    --ink: #141414;
    --photo-green: #4f7a3e;
    --photo-light: #d9d2c8;
  }
  html, body {
    margin: 0;
    padding: 0;
    width: 1200px;
    height: 900px;
    overflow: hidden;
    background: var(--backdrop);
    font-family: "Delius", "Comic Sans MS", sans-serif;
    color: var(--ink);
  }
  .card {
    position: absolute;
    width: 560px;
    height: 320px;
    border-radius: 3px;
    box-shadow: 0 14px 30px rgba(0,0,0,.45);
    box-sizing: border-box;
    overflow: hidden;
  }
  .card--front {
    left: 320px;
    top: 90px;
    background: var(--peach);
    display: flex;
    flex-direction: column;
    align-items: center;
    justify-content: center;
    gap: 14px;
  }
  .brand-name {
    margin: 0;
    font-size: 40px;
    font-weight: 400;
    letter-spacing: .5px;
  }
  .web-pill {
    background: var(--sky-pill);
    border-radius: 4px;
    padding: 3px 16px;
    font-size: 14px;
    letter-spacing: .6px;
  }
  .card--back {
    left: 320px;
    top: 490px;
    background: var(--sky);
  }
  .portrait {
    position: absolute;
    left: 50px;
    top: 60px;
    width: 200px;
    height: 200px;
    border-radius: 50%;
    border: 8px solid var(--peach-ring);
    box-sizing: border-box;
    background: radial-gradient(circle at 65% 55%, var(--photo-light) 0 28%, var(--photo-green) 60%);
  }
  .contact {
    position: absolute;
    left: 276px;
    right: 20px;
    top: 58px;
    font-size: 17px;
    line-height: 1.3;
  }
  .contact p { margin: 0; white-space: nowrap; }
  .contact .contact-name { margin-bottom: 22px; }
  .contact .contact-city { margin-top: 24px; }
</style>
</head>
<body>
  <section class="card card--front">
    <h1 class="brand-name">Paws Unwound Studio</h1>
    <div class="web-pill">www.Pawsunwoundstudio.com</div>
  </section>

  <section class="card card--back">
    <div class="portrait" role="img" aria-label="Photo of the therapist with a large dog on a lawn"></div>
    <div class="contact">
      <p class="contact-name">Paws Unwound Studio</p>
      <p class="contact-phone">614.382.5097</p>
      <p class="contact-email">Rulo@Pawsunwoundstudio.com</p>
      <p class="contact-city">Cedar Hollow, TN</p>
    </div>
  </section>
</body>
</html>
```